General Dental Office Business Card

I run a private general dental office in southern California, and would like a refresh/redesign of my business card. I focus on quality care rather than volume. The email address on the uploaded current card should be updated to: info@marbleshoredental.example. The current card's logo is a deboss, but I am open to other ideas. The logo can be refreshed, but it is something that's been with me since the beginning of the office, so I wouldn't want a drastic redesign.
Target Market(s)
Adults 18-99, whoever needs dental services
Industry/Entity Type
Healthcare/Dental
Contact Information for Business Card
Name, Address, Phone, email
Colors
Designer to choose colors to be used in the design.
Requirements
Must have
- Logo (Same as original one in the uploaded file), space on back for appointment time/date

```html
<!DOCTYPE html>
<html lang="en">
<head>
<meta charset="utf-8">
<title>Marble Shore Dental – Business Card</title>
<link href="https://fonts.googleapis.com/css2?family=Jost:wght@400;500;600&display=swap" rel="stylesheet">
<style>
  :root {
    --navy: #1c4b72;
    --sky: #5cbde3;
    --ink: #3f4348;
    --paper: #ffffff;
    --paper-shade: #f1f2f3;
    --backdrop: #dfe2e5;
    --photo-a: #b9b6b2;
    --photo-b: #6d6a67;
  }
  * { box-sizing: border-box; margin: 0; padding: 0; }
  html, body {
    width: 1200px; height: 900px; overflow: hidden;
    background: var(--backdrop);
    font-family: "Jost", sans-serif;
  }
  .stage {
    position: relative; width: 1200px; height: 900px;
    display: flex; justify-content: center; align-items: center; gap: 60px;
  }
  .card {
    position: relative; width: 400px; height: 700px;
    background: linear-gradient(160deg, var(--paper) 55%, var(--paper-shade));
    box-shadow: 0 10px 30px rgba(0,0,0,.18);
    overflow: hidden;
  }

  /* front */
  .brand {
    position: absolute; left: 34px; top: 46px;
    display: flex; align-items: center; gap: 14px;
  }
  .brand-dot {
    width: 74px; height: 74px; border-radius: 50%;
    border: 5px solid var(--navy);
  }
  .brand-name {
    color: var(--navy); font-weight: 400; font-size: 34px; line-height: 1.02;
    letter-spacing: 1px; text-transform: uppercase;
  }
  .portrait {
    position: absolute; left: 50%; top: 186px; transform: translateX(-50%);
    width: 168px; height: 168px; border-radius: 50%;
    border: 2px solid var(--sky); padding: 5px;
  }
  .portrait-fill {
    width: 100%; height: 100%; border-radius: 50%;
    background: radial-gradient(circle at 50% 40%, var(--photo-a), var(--photo-b));
  }
  .person { position: absolute; top: 372px; width: 100%; text-align: center; }
  .person-name { color: var(--navy); font-weight: 600; font-size: 25px; }
  .person-role { color: var(--ink); font-size: 19px; margin-top: 2px; }

  .divider {
    position: absolute; left: 30px; right: 30px;
    display: flex; align-items: center; gap: 8px;
  }
  .divider::before, .divider::after {
    content: ""; flex: 1; height: 1.5px; background: var(--navy);
  }
  .divider.first { top: 444px; }
  .divider.second { top: 566px; }
  .icon {
    width: 34px; height: 34px; border-radius: 50%; background: var(--navy);
    display: flex; align-items: center; justify-content: center;
  }
  .icon svg { width: 18px; height: 18px; }
  .contact {
    position: absolute; width: 100%; text-align: center;
    color: var(--ink); font-size: 19px; line-height: 1.3;
  }
  .contact.address { top: 488px; }
  .contact.online { top: 612px; font-size: 18px; }

  /* back */
  .appointment { position: absolute; left: 34px; top: 54px; right: 34px; }
  .appointment-title {
    color: var(--navy); font-weight: 600; font-size: 24px; letter-spacing: 1px;
    text-transform: uppercase; padding-bottom: 8px;
    border-bottom: 2px dotted var(--sky);
  }
  .field {
    display: flex; align-items: flex-end; gap: 8px; margin-top: 28px;
    color: var(--sky); font-size: 20px;
  }
  .field .blank { flex: 1; border-bottom: 2px dotted var(--sky); margin-bottom: 6px; }
  .field.time .blank { flex: 0 0 250px; }
  .side-brand {
    position: absolute; right: 30px; bottom: 40px;
    display: flex; flex-direction: column; align-items: center; gap: 14px;
  }
  .side-brand .brand-name {
    writing-mode: vertical-rl; transform: rotate(180deg);
    font-size: 36px;
  }
</style>
</head>
<body>
<main class="stage">

  <section class="card card-front">
    <div class="brand">
      <span class="brand-dot"></span>
      <span class="brand-name">Marble<br>Shore Dental</span>
    </div>

    <div class="portrait">
      <div class="portrait-fill" role="img" aria-label="Portrait photograph of the dentist"></div>
    </div>

    <div class="person">
      <p class="person-name">Dr. Evan T. Park DDS</p>
      <p class="person-role">General Dentistry</p>
    </div>

    <div class="divider first">
      <span class="icon" aria-label="Phone">
        <svg viewBox="0 0 24 24" fill="none" stroke="#fff" stroke-width="2" stroke-linecap="round" stroke-linejoin="round"><path d="M5 3h4l2 5-2.5 1.5a11 11 0 0 0 6 6L16 13l5 2v4a2 2 0 0 1-2 2A16 16 0 0 1 3 5a2 2 0 0 1 2-2z"/></svg>
      </span>
      <span class="icon" aria-label="Location">
        <svg viewBox="0 0 24 24" fill="none" stroke="#fff" stroke-width="2"><path d="M12 22s7-7 7-12a7 7 0 0 0-14 0c0 5 7 12 7 12z"/><circle cx="12" cy="10" r="2.5"/></svg>
      </span>
    </div>

    <div class="contact address">
      <p>(555) 014-2371</p>
      <p>2180 Seabright Avenue</p>
      <p>Marble Shore, CA 90000</p>
    </div>

    <div class="divider second">
      <span class="icon" aria-label="Email">
        <svg viewBox="0 0 24 24" fill="none" stroke="#fff" stroke-width="2"><rect x="3" y="6" width="18" height="12" rx="1"/><path d="M3 7l9 6 9-6"/></svg>
      </span>
      <span class="icon" aria-label="Website">
        <svg viewBox="0 0 24 24" fill="none" stroke="#fff" stroke-width="1.8"><circle cx="12" cy="12" r="9"/><path d="M3 12h18M12 3c3 3 3 15 0 18M12 3c-3 3-3 15 0 18"/></svg>
      </span>
    </div>

    <div class="contact online">
      <p>info@marbleshoredental.example</p>
      <p>www.marbleshoredental.example</p>
    </div>
  </section>

  <section class="card card-back">
    <div class="appointment">
      <h2 class="appointment-title">Your Appointment</h2>
      <p class="field date">Date <span class="blank"></span></p>
      <p class="field time">Time <span class="blank"></span></p>
    </div>

    <div class="side-brand">
      <span class="brand-name">Marble<br>Shore Dental</span>
      <span class="brand-dot"></span>
    </div>
  </section>

</main>
</body>
</html>
```